Box Truck Wrap

We need to create a design for our 26' box trucks. We want it to be very attention grabbing yet simple and we would like it to be modeled after our existing branding. The final deliverable needs to be 75DPI (Or more) at scale. The size of the wrap will be approximately 26' long and 8' tall. Colors are red white and blue. Please no stock images and we dpnt want any photos of people. Examples of other company trucks are included. We need one design for the side and also one for the back. Approx 7' x 8'

```html
<!DOCTYPE html>
<html lang="en">
<head>
<meta charset="utf-8">
<title>Ridgeline Movers – Box Truck Wrap</title>
<link rel="stylesheet" href="https://fonts.googleapis.com/css2?family=Montserrat:wght@700;800&family=Poppins:wght@600&display=swap">
<style>
  :root {
    --red: #e90f0f;
    --red-light: #f43a3a;
    --navy: #150a68;
    --white: #ffffff;
    --gold: #f2c521;
    --backdrop: #9a9a9a;
  }
  html, body { margin: 0; padding: 0; overflow: hidden; }
  .canvas {
    position: relative;
    width: 748px;
    height: 1200px;
    background: var(--backdrop);
    overflow: hidden;
    font-family: "Montserrat", sans-serif;
  }
  .panel {
    position: absolute;
    background: linear-gradient(180deg, var(--red-light) 0%, var(--red) 30%, var(--red) 100%);
    overflow: hidden;
  }
  .panel svg.shapes { position: absolute; inset: 0; }
  .side { width: 651px; height: 178px; }
  .side--driver { left: 73px; top: 47px;
    clip-path: polygon(0 0, 100% 0, 100% 100%, 102px 100%, 102px 67px, 0 67px); }
  .side--curb { left: 24px; top: 366px;
    clip-path: polygon(0 0, 100% 0, 100% 67px, 544px 67px, 544px 100%, 0 100%); }
  .back { left: 174px; top: 686px; width: 402px; height: 406px; }

  .mountain-art {
    position: absolute;
    background: radial-gradient(ellipse at 50% 60%, rgba(255,255,255,.9) 0%, rgba(255,255,255,.55) 40%, rgba(255,255,255,0) 72%);
  }
  .wordmark {
    position: absolute;
    color: var(--navy);
    font-weight: 800;
    line-height: 1;
    white-space: nowrap;
  }
  .wordmark__main { display: block; font-size: 30px; letter-spacing: 4px; }
  .wordmark__sub { display: block; font-size: 17px; letter-spacing: 13px; margin-top: 6px; margin-left: 40px; }

  .brand-badge {
    position: absolute;
    width: 128px; height: 128px;
    border-radius: 50%;
    background: var(--navy);
    display: flex; align-items: center; justify-content: center;
    color: var(--white);
    font-weight: 800;
    font-size: 15px;
    letter-spacing: 1px;
  }
  .phone {
    position: absolute;
    color: var(--white);
    font-family: "Poppins", sans-serif;
    font-weight: 600;
    font-size: 18px;
    white-space: nowrap;
    line-height: 1;
  }
  .web {
    position: absolute;
    color: var(--white);
    font-weight: 800;
    font-size: 10px;
    white-space: nowrap;
    line-height: 1;
  }
  .stars { position: absolute; width: 78px; height: 14px; }

  .tagline {
    position: absolute;
    left: 0; right: 0; top: 292px;
    text-align: center;
    color: var(--white);
    font-weight: 800;
    font-size: 17px;
    line-height: 1.12;
  }
  .contact-band {
    position: absolute;
    left: 0; right: 0; top: 331px; height: 30px;
    background: var(--red);
    color: var(--white);
    font-family: "Poppins", sans-serif;
    font-weight: 600;
    font-size: 17px;
    display: flex; align-items: center; justify-content: center;
    white-space: nowrap;
  }
</style>
</head>
<body>
<div class="canvas">

  <svg width="0" height="0" style="position:absolute">
    <defs>
      <polygon id="star" points="7,0 8.7,5 14,5 9.7,8.1 11.3,13.2 7,10.1 2.7,13.2 4.3,8.1 0,5 5.3,5" fill="#f2c521"/>
      <g id="star-row">
        <use href="#star" x="0"/><use href="#star" x="16"/><use href="#star" x="32"/><use href="#star" x="48"/><use href="#star" x="64"/>
      </g>
    </defs>
  </svg>

  <!-- Driver side -->
  <section class="panel side side--driver" aria-label="Driver side wrap">
    <div class="mountain-art" role="img" aria-label="Snow-capped mountain range illustration" style="left:105px;top:8px;width:470px;height:170px;"></div>
    <svg class="shapes" viewBox="0 0 651 178" width="651" height="178">
      <path fill="var(--navy)" d="M102 178 L102 170 C150 135 190 123 233 123 C290 123 330 160 371 173 C420 150 470 126 535 126 C590 126 625 150 651 165 L651 178 Z"/>
      <path fill="none" stroke="var(--white)" stroke-width="1.2" stroke-dasharray="5 3" d="M110 170 C155 137 192 130 233 130 C288 130 328 164 371 180 M371 180 C420 157 470 133 535 133 C588 133 622 155 651 172"/>
    </svg>
    <svg class="stars" viewBox="0 0 78 14" style="left:567px;top:10px;"><use href="#star-row"/></svg>
    <div class="wordmark" style="left:118px;top:58px;">
      <span class="wordmark__main">RIDGELINE</span>
      <span class="wordmark__sub">MOVERS</span>
    </div>
    <div class="brand-badge" style="left:471px;top:30px;">RIDGELINE</div>
    <div class="web" style="left:168px;top:154px;">RidgelineMoversTX.com</div>
    <div class="phone" style="left:470px;top:148px;">(555) 214-0397</div>
  </section>

  <!-- Curb side -->
  <section class="panel side side--curb" aria-label="Curb side wrap">
    <div class="mountain-art" role="img" aria-label="Snow-capped mountain range illustration" style="left:150px;top:8px;width:420px;height:170px;"></div>
    <svg class="shapes" viewBox="0 0 651 178" width="651" height="178">
      <path fill="var(--navy)" d="M0 178 L0 165 C30 140 70 124 115 124 C170 124 215 160 253 173 C300 150 350 124 416 124 C470 124 515 155 544 170 L544 178 Z"/>
      <path fill="none" stroke="var(--white)" stroke-width="1.2" stroke-dasharray="5 3" d="M0 172 C30 147 70 131 115 131 C168 131 212 165 253 180 M253 180 C300 157 350 131 416 131 C468 131 512 160 544 177"/>
    </svg>
    <svg class="stars" viewBox="0 0 78 14" style="left:10px;top:10px;"><use href="#star-row"/></svg>
    <div class="brand-badge" style="left:51px;top:14px;">RIDGELINE</div>
    <div class="wordmark" style="left:300px;top:58px;">
      <span class="wordmark__main">RIDGELINE</span>
      <span class="wordmark__sub">MOVERS</span>
    </div>
    <div class="phone" style="left:48px;top:146px;">(555) 214-0397</div>
    <div class="web" style="left:350px;top:154px;">RidgelineMoversTX.com</div>
  </section>

  <!-- Rear doors -->
  <section class="panel back" aria-label="Rear door wrap">
    <div class="mountain-art" role="img" aria-label="Snow-capped mountain range illustration" style="left:0;top:120px;width:402px;height:160px;"></div>
    <svg class="shapes" viewBox="0 0 402 406" width="402" height="406">
      <path fill="var(--navy)" d="M0 265 C20 250 45 240 78 240 C120 240 160 265 192 274 C225 260 265 240 305 240 C345 240 380 255 402 268 L402 406 L0 406 Z"/>
      <path fill="none" stroke="var(--white)" stroke-width="1.2" stroke-dasharray="5 3" d="M0 258 C20 243 45 233 78 233 C120 233 160 258 192 267 C225 253 265 233 305 233 C345 233 380 248 402 261"/>
    </svg>
    <svg class="stars" viewBox="0 0 78 14" style="left:297px;top:30px;width:98px;height:17px;"><use href="#star-row"/></svg>
    <div class="wordmark" style="left:12px;top:96px;">
      <span class="wordmark__main" style="letter-spacing:3px;">RIDGELINE</span>
      <span class="wordmark__sub" style="margin-left:36px;">MOVERS</span>
    </div>
    <div class="brand-badge" style="left:244px;top:64px;">RIDGELINE</div>
    <div class="tagline">HIGHLY-TRAINED LOCAL &amp;<br>LONG DISTANCE MOVERS</div>
    <div class="contact-band">(555) 214-0397 | RidgelineMoversTX.com</div>
  </section>

</div>
</body>
</html>
```